Introducing Vessa – the virtual restaurant experience at home

Missing going out on dining at your favourite restaurant with your friends, then Vessa Dining is the answer.

While it may not be possible during the COVID-19 pandemic, or when restaurants return as booking opportunities will be hard to get, an innovative new concept gives people the chance to enjoy a virtual restaurant experience at home.

VESSA offers diners the ability to get the restaurant experience at home and restaurants to expand their dining rooms beyond the confines of social distancing

Vessa Dining is an app where you can book your favourite restaurant table, invite your friends and choose your menu and beverages. On the day the restaurant will come to your house, set your table, cook and serve you the menu you have chosen, serve you drinks and clean up, just like you where at the restaurant.

We are looking for 2 similar infographics to explain a process from 2 different perspective

The design needs to be simple, contemporary, imaginative and modern for this concept, it needs to be sophisticated, something that would represent an up-market to fine dining style of restaurant. The designs need to be easily understood using white space to separate the elements

Our preferred colour is attached along with our logos

Infographic 1 - Host Process
1. Host makes reservation at favourite restaurant at home on the Vessa Dining App
2. Select menus and invite guests
3. Confirm either single or shared payment options
4. Booking confirmed with restaurant
5. Host confirms on the App they the required equipment
6. Cook/server arrive 1 hour prior to guests, prepares and sets table
7. Guests arrive and cook/server offer dinks and serves meal
8. Cook/Server cleans up and finalises check with host

Infographic 2 - Restaurant Process
1. Host makes reservation and orders meal
2. Restaurant confirm reservation details
3. Restaurant prepares cuisine and arranges cook/serve waiter
4. Cook/server arrive 1 hour before guests, prepares and sets table
5. Cook/server cooks and serves meals and wine
6. Cook/Server cleans up and finalises check with host

Good Luck

```html
<!DOCTYPE html>
<html lang="en">
<head>
<meta charset="utf-8">
<title>Vessa Dining – Host and Restaurant Process</title>
<link href="https://fonts.googleapis.com/css2?family=Jost:wght@400;500&display=swap" rel="stylesheet">
<style>
  :root {
    --paper: #ffffff;
    --panel: #000000;
    --ink: #ffffff;
    --gold: #b8915f;
  }
  * { box-sizing: border-box; margin: 0; padding: 0; }
  html, body { width: 1104px; height: 1200px; overflow: hidden; background: var(--paper); }
  body { position: relative; font-family: "Jost", "Futura", sans-serif; color: var(--ink); }

  .process {
    position: absolute;
    top: 60px;
    height: 1081px;
    background: var(--panel);
  }
  .process--host { left: 0; width: 400px; }
  .process--restaurant { left: 708px; width: 396px; }

  .process__title {
    position: absolute;
    top: 16px;
    left: 0; right: 0;
    text-align: center;
    font-weight: 400;
    font-size: 29px;
    letter-spacing: 0.2px;
  }

  .steps { list-style: none; }
  .step {
    position: absolute;
    left: 0; right: 0;
    height: 126px;
  }
  .step__number {
    position: absolute;
    top: 50%;
    transform: translateY(-52%);
    font-size: 54px;
    font-weight: 400;
    line-height: 1;
  }
  .step__text {
    position: absolute;
    top: 50%;
    transform: translateY(-50%);
    font-size: 11.5px;
    line-height: 14px;
    white-space: nowrap;
  }
  .step__icon {
    position: absolute;
    top: 0;
    width: 126px;
    height: 126px;
  }
  .process--host .step__number { left: 36px; }
  .process--host .step__text { left: 78px; }
  .process--host .step__text--wide { left: 72px; }
  .process--restaurant .step__number { left: 32px; }
  .process--restaurant .step__text { left: 72px; }

  .icon-frame { fill: none; stroke: var(--gold); stroke-width: 1.2; }
  .icon-line { fill: none; stroke: var(--ink); }
  .icon-fill { fill: var(--ink); }
  .icon-cut { fill: var(--panel); }
  .icon-label { fill: var(--ink); font-family: "Jost", sans-serif; font-size: 10px; }
</style>
</head>
<body>

<svg width="0" height="0" style="position:absolute" aria-hidden="true">
  <defs>
    <symbol id="frame" viewBox="0 0 126 126">
      <polygon class="icon-frame" points="63,1 125,63 63,125 1,63"/>
    </symbol>
    <symbol id="icon-bowl" viewBox="0 0 126 126">
      <ellipse class="icon-line" cx="63" cy="44" rx="26" ry="8" stroke-width="4.5"/>
      <ellipse class="icon-line" cx="63" cy="62" rx="26" ry="7" stroke-width="4.5"/>
      <path class="icon-fill" d="M35,66 Q63,78 91,66 A28,24 0 0 1 35,66 Z"/>
    </symbol>
    <symbol id="icon-menu" viewBox="0 0 126 126">
      <rect class="icon-line" x="40" y="32" width="46" height="60" rx="5" stroke-width="3.5"/>
      <text class="icon-label" x="63" y="48" text-anchor="middle">MENU</text>
      <circle class="icon-fill" cx="48" cy="57" r="3"/><line class="icon-line" x1="54" y1="57" x2="78" y2="56" stroke-width="2"/>
      <circle class="icon-fill" cx="48" cy="68" r="3"/><line class="icon-line" x1="54" y1="68" x2="78" y2="67" stroke-width="2"/>
      <circle class="icon-fill" cx="48" cy="79" r="3"/><line class="icon-line" x1="54" y1="79" x2="78" y2="78" stroke-width="2"/>
    </symbol>
    <symbol id="icon-details" viewBox="0 0 126 126">
      <rect class="icon-line" x="40" y="32" width="46" height="60" rx="5" stroke-width="3.5"/>
      <text class="icon-label" x="63" y="48" text-anchor="middle" font-size="9.5">DETAILS</text>
      <circle class="icon-fill" cx="48" cy="57" r="3"/><line class="icon-line" x1="54" y1="57" x2="78" y2="57" stroke-width="2"/>
      <circle class="icon-fill" cx="48" cy="68" r="3"/><line class="icon-line" x1="54" y1="68" x2="78" y2="68" stroke-width="2"/>
      <circle class="icon-fill" cx="48" cy="79" r="3"/><line class="icon-line" x1="54" y1="79" x2="78" y2="79" stroke-width="2"/>
    </symbol>
    <symbol id="icon-payment" viewBox="0 0 126 126">
      <rect class="icon-line" x="52" y="34" width="30" height="50" stroke-width="2.5"/>
      <rect class="icon-cut" x="48" y="38" width="30" height="50"/>
      <rect class="icon-line" x="48" y="38" width="30" height="50" stroke-width="2.5"/>
      <rect class="icon-cut" x="42" y="42" width="32" height="52"/>
      <rect class="icon-line" x="42" y="42" width="32" height="52" stroke-width="3"/>
      <ellipse class="icon-line" cx="58" cy="68" rx="11" ry="9" stroke-width="2.5"/>
      <text class="icon-label" x="58" y="73" text-anchor="middle" font-size="15">$</text>
    </symbol>
    <symbol id="icon-tick" viewBox="0 0 126 126">
      <circle class="icon-line" cx="60" cy="69" r="27" stroke-width="4"/>
      <path class="icon-line" d="M48,67 L59,79 L85,40" stroke-width="6"/>
    </symbol>
    <symbol id="icon-board" viewBox="0 0 126 126">
      <rect class="icon-fill" x="31" y="42" width="64" height="42" rx="4"/>
      <rect class="icon-cut" x="37" y="54" width="5" height="17" rx="2.5"/>
    </symbol>
    <symbol id="icon-table" viewBox="0 0 126 126">
      <circle class="icon-fill" cx="63" cy="59" r="27"/>
      <circle class="icon-cut" cx="63" cy="59" r="22"/>
      <circle class="icon-fill" cx="63" cy="59" r="20.5"/>
      <path class="icon-line" d="M28,42 V56 M31,42 V56 M34,42 V56 M28,56 H34 M31,56 V86" stroke-width="1.8"/>
      <path class="icon-fill" d="M96,42 Q102,55 99,66 V86 H96 Z"/>
    </symbol>
    <symbol id="icon-serve" viewBox="0 0 126 126">
      <path class="icon-fill" d="M26,48 H38 Q40,64 32,66 Q24,64 26,48 Z"/>
      <line class="icon-line" x1="32" y1="66" x2="32" y2="82" stroke-width="2"/>
      <line class="icon-line" x1="27" y1="82" x2="37" y2="82" stroke-width="2"/>
      <circle class="icon-fill" cx="71" cy="50" r="4"/>
      <path class="icon-fill" d="M45,80 A26,27 0 0 1 97,80 Z"/>
      <rect class="icon-fill" x="42" y="81" width="58" height="3"/>
    </symbol>
    <symbol id="icon-check-left" viewBox="0 0 126 126">
      <rect class="icon-line" x="54" y="33" width="32" height="58" stroke-width="3.5"/>
      <text class="icon-label" transform="translate(75,62) rotate(-90)" text-anchor="middle" font-size="12">CHECK</text>
      <path class="icon-fill" d="M24,61 H36 L42,56 H66 V63 H58 V72 L44,76 H24 Z"/>
    </symbol>
    <symbol id="icon-check-right" viewBox="0 0 126 126">
      <rect class="icon-line" x="40" y="33" width="32" height="58" stroke-width="3.5"/>
      <text class="icon-label" transform="translate(61,62) rotate(-90)" text-anchor="middle" font-size="12">CHECK</text>
      <path class="icon-fill" d="M102,56 H90 L84,51 H60 V58 H68 V67 L82,71 H102 Z"/>
    </symbol>
    <symbol id="icon-chef" viewBox="0 0 126 126">
      <circle class="icon-fill" cx="50" cy="53" r="11"/>
      <circle class="icon-fill" cx="63" cy="46" r="13"/>
      <circle class="icon-fill" cx="76" cy="53" r="11"/>
      <rect class="icon-fill" x="49" y="54" width="28" height="28"/>
      <rect class="icon-fill" x="46" y="85" width="34" height="4" rx="2"/>
    </symbol>
  </defs>
</svg>

<section class="process process--host">
  <h2 class="process__title">Host Process</h2>
  <ol class="steps">
    <li class="step" style="top:134px">
      <span class="step__number">1</span>
      <p class="step__text step__text--wide">Host makes reservation at<br>favourite restaurant at home<br>on the Vessa Dining App</p>
      <svg class="step__icon" style="left:247px" viewBox="0 0 126 126" aria-hidden="true"><use href="#frame"/><use href="#icon-bowl"/></svg>
    </li>
    <li class="step" style="top:248px">
      <span class="step__number">2</span>
      <p class="step__text">Select menus and<br>invite guests</p>
      <svg class="step__icon" style="left:219px" viewBox="0 0 126 126" aria-hidden="true"><use href="#frame"/><use href="#icon-menu"/></svg>
    </li>
    <li class="step" style="top:361px">
      <span class="step__number">3</span>
      <p class="step__text">Confirm either single or<br>shared payment options</p>
      <svg class="step__icon" style="left:247px" viewBox="0 0 126 126" aria-hidden="true"><use href="#frame"/><use href="#icon-payment"/></svg>
    </li>
    <li class="step" style="top:475px">
      <span class="step__number">4</span>
      <p class="step__text" style="left:81px">Booking confirmed with<br>restaurant</p>
      <svg class="step__icon" style="left:219px" viewBox="0 0 126 126" aria-hidden="true"><use href="#frame"/><use href="#icon-tick"/></svg>
    </li>
    <li class="step" style="top:588px">
      <span class="step__number">5</span>
      <p class="step__text" style="left:80px">Host confirms on the<br>App they the required<br>equipment</p>
      <svg class="step__icon" style="left:247px" viewBox="0 0 126 126" aria-hidden="true"><use href="#frame"/><use href="#icon-board"/></svg>
    </li>
    <li class="step" style="top:702px">
      <span class="step__number">6</span>
      <p class="step__text">Cook/server arrive 1 hour<br>prior to guests, prepares<br>and sets table</p>
      <svg class="step__icon" style="left:219px" viewBox="0 0 126 126" aria-hidden="true"><use href="#frame"/><use href="#icon-table"/></svg>
    </li>
    <li class="step" style="top:815px">
      <span class="step__number">7</span>
      <p class="step__text">Guests arrive and<br>cook/server offer drinks<br>and serves meal</p>
      <svg class="step__icon" style="left:247px" viewBox="0 0 126 126" aria-hidden="true"><use href="#frame"/><use href="#icon-serve"/></svg>
    </li>
    <li class="step" style="top:929px">
      <span class="step__number">8</span>
      <p class="step__text">Cook/Server cleans up and<br>finalises check with host</p>
      <svg class="step__icon" style="left:219px" viewBox="0 0 126 126" aria-hidden="true"><use href="#frame"/><use href="#icon-check-left"/></svg>
    </li>
  </ol>
</section>

<section class="process process--restaurant">
  <h2 class="process__title">Restaurant Process</h2>
  <ol class="steps">
    <li class="step" style="top:134px">
      <span class="step__number">1</span>
      <p class="step__text" style="left:69px">Host makes reservation<br>and orders meal</p>
      <svg class="step__icon" style="left:241px" viewBox="0 0 126 126" aria-hidden="true"><use href="#frame"/><use href="#icon-bowl"/></svg>
    </li>
    <li class="step" style="top:248px">
      <span class="step__number">2</span>
      <p class="step__text" style="left:73px">Restaurant confirm<br>reservation details</p>
      <svg class="step__icon" style="left:213px" viewBox="0 0 126 126" aria-hidden="true"><use href="#frame"/><use href="#icon-details"/></svg>
    </li>
    <li class="step" style="top:361px">
      <span class="step__number">3</span>
      <p class="step__text">Restaurant prepares cuisine<br>and arranges cook/serve waiter</p>
      <svg class="step__icon" style="left:241px" viewBox="0 0 126 126" aria-hidden="true"><use href="#frame"/><use href="#icon-chef"/></svg>
    </li>
    <li class="step" style="top:475px">
      <span class="step__number">4</span>
      <p class="step__text" style="left:77px">Cook/server arrive 1 hour<br>before guests, prepares<br>and sets table</p>
      <svg class="step__icon" style="left:213px" viewBox="0 0 126 126" aria-hidden="true"><use href="#frame"/><use href="#icon-table"/></svg>
    </li>
    <li class="step" style="top:588px">
      <span class="step__number">5</span>
      <p class="step__text" style="left:75px">Cook/server cooks and<br>serves meals and wine</p>
      <svg class="step__icon" style="left:241px" viewBox="0 0 126 126" aria-hidden="true"><use href="#frame"/><use href="#icon-serve"/></svg>
    </li>
    <li class="step" style="top:702px">
      <span class="step__number">6</span>
      <p class="step__text">Cook/Server cleans up and<br>finalises check with host</p>
      <svg class="step__icon" style="left:213px" viewBox="0 0 126 126" aria-hidden="true"><use href="#frame"/><use href="#icon-check-right"/></svg>
    </li>
  </ol>
</section>

</body>
</html>
```